Business Card Design Project

I am looking for a minimal matte background/shiny (spot UV) ink monochromatic design with a splash of neon color.

the card should be 2 sided, logo only on one side - all info and possibly logo on the other.

My creative director described the colors he imagined for the design to be:
'it's a dark field, like charcoal or a really dark burgundy, or deep blue, shot through with a neon—but just a tiny bit of it. so a charcoal field with a laser-thin streak of electric lime, safety orange, or cobalt blue. really beautiful stuff.'

here are some samples of the types of cards I am trying to create:
http://www.pictavault.example/photos/dawnpress/6967376935/in/photostream -> Vandrelle Lustre

http://www.pictavault.example/photos/dawnpress/6497659409/in/photostream -> Standard Coated (14pt/matte) with SPOT UV

http://www.pictavault.example/photos/dawnpress/6497658995/in/photostream/ -> Heavy Corvane with Raised Ink

http://www.pictavault.example/photos/dawnpress/6275629165/in/photostream/ -> Standard Coated (14pt/matte) with SPOT UV

Here is my logo:
https://www.filecrate.example/s/sigym192mlh58ge/quillorb%20logotype%20final.ai

Here are the details for info:
Dorian Elwood Marsh
email - dorian@quillorb.example
mobile - 555 013 2867
web -
quillorb.example: inventive technology applications
quillorb-tv.example: innovative video advertising

please let me know if there is anything at all that you need.

Target Market(s)

mid to large agencies that require interactive design and entrepreneurial/startup individuals/companies that need application development.

Industry/Entity Type

Safety

Requirements
Must have
• logo only on one side

```html
<!DOCTYPE html>
<html lang="en">
<head>
<meta charset="utf-8">
<title>Quillorb Business Card</title>
<link rel="stylesheet" href="https://fonts.googleapis.com/css2?family=Marcellus&family=Oswald:wght@300&family=Arimo&display=swap">
<style>
  :root {
    --charcoal: #354350;
    --lime: #9dc33b;
    --ink: #111111;
    --paper: #ffffff;
    --rule-blue: #2b4a8c;
    --label: #1a1a1a;
    --card-edge: #bdbdbd;
    --pattern-light: #e9e9ec;
    --pattern-dark: #4a5866;
    --uv-pattern: #dcdcdc;
  }
  * { box-sizing: border-box; margin: 0; padding: 0; }
  html, body {
    width: 1200px; height: 1200px; overflow: hidden;
    background: var(--paper);
  }
  .board { position: relative; width: 1200px; height: 1200px; }
  .side-label {
    position: absolute; left: 375px;
    font: 20px "Arimo", Arial, sans-serif; color: var(--label);
  }
  .card {
    position: absolute; left: 372px; width: 474px; height: 288px;
    overflow: hidden; border: 1px solid var(--card-edge);
  }
  .card--front { top: 105px; background: var(--paper); }
  .card--back { top: 445px; background: var(--charcoal); border-color: var(--charcoal); }
  .card--uv { top: 800px; background: var(--paper); }

  .front-band { position: absolute; left: 0; top: 0; width: 100%; height: 20px; background: var(--charcoal); }

  .pattern { position: absolute; border-radius: 4px; }
  .card--front .pattern { background: linear-gradient(135deg, var(--pattern-light), #f6f6f8); }
  .card--back .pattern { background: linear-gradient(135deg, var(--pattern-dark), var(--charcoal)); }
  .card--uv .pattern { background: linear-gradient(135deg, var(--uv-pattern), #f1f1f1); }

  .holder-name {
    position: absolute; left: 60px; top: 106px;
    font: 17px "Marcellus", "Times New Roman", serif;
    letter-spacing: 1.2px; color: #1f2a3a; text-transform: uppercase;
    white-space: nowrap; line-height: 1.3;
  }
  .name-rule {
    position: absolute; left: 52px; top: 137px; width: 190px; height: 2px;
    background: linear-gradient(90deg, transparent, var(--rule-blue) 40%, var(--rule-blue) 60%, transparent);
  }
  .contact-list {
    position: absolute; left: 155px; top: 171px; list-style: none;
    font: 12px "Arimo", Arial, sans-serif; color: #222;
  }
  .contact-list li { display: flex; align-items: center; height: 20.5px; white-space: nowrap; }
  .contact-icon { width: 15px; height: 15px; margin-right: 6px; flex: none; }
  .contact-list .no-icon { padding-left: 21px; }

  .wordmark {
    position: absolute; left: 120px; top: 144px; transform: translateY(-50%);
    font: 300 46px "Oswald", "Arial Narrow", sans-serif;
    letter-spacing: 6px; text-transform: uppercase; line-height: 1;
  }
  .card--back .wordmark { color: var(--lime); }
  .card--uv .wordmark { color: var(--ink); }
</style>
</head>
<body>
<main class="board">

  <p class="side-label" style="top:78px;">Front</p>
  <section class="card card--front">
    <div class="front-band"></div>
    <div class="pattern" role="img" aria-label="Linked hexagon outline pattern" style="left:270px;top:20px;width:204px;height:120px;"></div>
    <div class="pattern" role="img" aria-label="Linked hexagon outline pattern" style="left:0;top:195px;width:92px;height:93px;"></div>
    <p class="holder-name">Dorian Elwood Marsh</p>
    <div class="name-rule"></div>
    <ul class="contact-list">
      <li>
        <svg class="contact-icon" viewBox="0 0 16 16"><circle cx="8" cy="8" r="8" fill="var(--lime)"/><path d="M5 4.5l1.6-.5 1 2.2-1 .8a5 5 0 0 0 2.4 2.4l.8-1 2.2 1-.5 1.6c-3.6.3-6.8-2.9-6.5-6.5z" fill="#fff"/></svg>
        555 013 2867
      </li>
      <li>
        <svg class="contact-icon" viewBox="0 0 16 16"><circle cx="8" cy="8" r="8" fill="var(--lime)"/><rect x="4" y="5" width="8" height="6" fill="none" stroke="#fff" stroke-width="1.2"/><path d="M4 5l4 3.5L12 5" fill="none" stroke="#fff" stroke-width="1.2"/></svg>
        dorian@quillorb.example
      </li>
      <li>
        <svg class="contact-icon" viewBox="0 0 16 16"><circle cx="8" cy="8" r="8" fill="var(--lime)"/><circle cx="8" cy="8" r="4.5" fill="none" stroke="#fff" stroke-width="1.1"/><ellipse cx="8" cy="8" rx="2" ry="4.5" fill="none" stroke="#fff" stroke-width="1"/><path d="M3.5 8h9" stroke="#fff" stroke-width="1"/></svg>
        quillorb.example: inventive technology applications
      </li>
      <li class="no-icon">quillorb-tv.example: innovative video advertising</li>
    </ul>
  </section>

  <p class="side-label" style="top:415px;">Back</p>
  <section class="card card--back">
    <div class="pattern" role="img" aria-label="Faint linked hexagon outline pattern" style="left:200px;top:0;width:274px;height:288px;opacity:.6;"></div>
    <div class="pattern" role="img" aria-label="Faint linked hexagon outline pattern" style="left:0;top:70px;width:150px;height:218px;opacity:.6;"></div>
    <p class="wordmark">Quillorb</p>
  </section>

  <p class="side-label" style="top:770px;">Spot UV</p>
  <section class="card card--uv">
    <div class="pattern" role="img" aria-label="Spot UV linked hexagon outline pattern" style="left:200px;top:0;width:274px;height:288px;"></div>
    <div class="pattern" role="img" aria-label="Spot UV linked hexagon outline pattern" style="left:0;top:70px;width:150px;height:218px;"></div>
    <p class="wordmark">Quillorb</p>
  </section>

</main>
</body>
</html>
```